Industrial Company-Pop-Up Banner Design for Demolition and Infrastructure Company

Hi-
We need to create 2 pop-up banners for our company. They will both have the same logo, but different photos. We would like to have the colors white, red, and black and feature a modern design. I have attached some inspiration photos.

Target Market(s)

Trade Show/Job Fair Audience

Industry/Entity Type

construction, industrial

Font styles to use
Sans Serif

Colors
EB3D1F
EC4F4E
F09395
F8D3D4
FCEDEE

Requirements
Must have
• 2 versions, each with different photos but same design. Logo, Red, Black, and White Color Scheme, Modern Design
Nice to have
• Modern Design similar to the inspiration photos

```html
<!DOCTYPE html>
<html lang="en">
<head>
<meta charset="utf-8">
<title>R.K. Halden Companies – Pop-Up Banners</title>
<link rel="stylesheet" href="https://fonts.googleapis.com/css2?family=Oswald:wght@600;700&family=Roboto:wght@700&display=swap">
<style>
  :root {
    --red: #d8222a;
    --black: #1c1c1c;
    --white: #ffffff;
    --stage: #959595;
  }
  * { margin: 0; padding: 0; box-sizing: border-box; }
  html, body { width: 1197px; height: 1200px; overflow: hidden; background: var(--stage); }
  .stage { position: relative; width: 1197px; height: 1200px; }
  .banner {
    position: absolute; top: 228px;
    width: 469px; height: 783px;
    background: var(--white);
    transform: scale(0.957); transform-origin: top left;
    overflow: hidden;
    font-family: "Oswald", "Arial Narrow", sans-serif;
    text-align: center;
  }
  .banner--first { left: 115px; }
  .banner--second { left: 633px; }
  .banner__topbar { position: absolute; left: 0; top: 0; width: 100%; height: 23px; background: var(--red); }
  .brand {
    position: absolute; left: 0; top: 62px; width: 100%;
    font-family: "Roboto", Arial, sans-serif; font-weight: 700;
    color: var(--red); line-height: 1.1;
  }
  .brand__name { display: block; font-size: 24px; letter-spacing: 0.5px; }
  .brand__sub { display: block; font-size: 15px; }
  .headline { position: absolute; left: 0; width: 100%; font-weight: 700; text-transform: uppercase; line-height: 1; }
  .headline--lead { top: 150px; font-size: 40px; color: var(--black); letter-spacing: 0.3px; }
  .headline--main { top: 183px; font-size: 94px; color: var(--red); letter-spacing: 1px; }
  .headline--since { top: 270px; font-size: 44px; color: var(--black); letter-spacing: 1px; }
  .rule { position: absolute; top: 295px; height: 3px; width: 58px; background: var(--red); }
  .rule--left { left: 62px; }
  .rule--right { left: 349px; }
  .phone {
    position: absolute; left: 103px; top: 347px; width: 262px; height: 44px;
    background: var(--red); color: var(--white);
    display: flex; align-items: center; justify-content: center; gap: 8px;
    font-size: 28px; font-weight: 600; letter-spacing: 1px;
  }
  .phone svg { width: 24px; height: 24px; }
  .graphic { position: absolute; left: 0; top: 0; width: 469px; height: 783px; }
  .graphic--mirrored { transform: scaleX(-1); }
  .website {
    position: absolute; left: 0; top: 728px; width: 100%;
    font-size: 19px; font-weight: 600; letter-spacing: 2.5px; color: var(--red);
  }
  .website__rule { position: absolute; left: 211px; top: 757px; width: 48px; height: 2px; background: var(--black); }
</style>
</head>
<body>
<main class="stage">

  <section class="banner banner--first">
    <div class="banner__topbar"></div>
    <div class="brand"><span class="brand__name">R.K. HALDEN</span><span class="brand__sub">Companies</span></div>
    <h2 class="headline headline--lead">Shaping America’s</h2>
    <h1 class="headline headline--main">Skyline</h1>
    <p class="headline headline--since">Since 1959</p>
    <span class="rule rule--left"></span><span class="rule rule--right"></span>
    <div class="phone">
      <svg viewBox="0 0 24 24" aria-hidden="true"><circle cx="12" cy="12" r="12" fill="#fff"/><path d="M8.2 6.5l1.9-.4 1.2 3-1.3 1c.6 1.4 1.6 2.5 3 3.2l1-1.3 3 1.2-.4 1.9c-4.4.4-8.7-3.9-8.4-8.6z" fill="#d8222a"/></svg>
      <span>888-555-0142</span>
    </div>
    <svg class="graphic" viewBox="0 0 469 783">
      <defs>
        <linearGradient id="a-plant" x1="0" y1="0" x2="0" y2="1"><stop offset="0" stop-color="#b9cde0"/><stop offset="1" stop-color="#5d6f84"/></linearGradient>
        <linearGradient id="a-site" x1="0" y1="0" x2="0" y2="1"><stop offset="0" stop-color="#9fb7c8"/><stop offset="0.5" stop-color="#5d8a9a"/><stop offset="1" stop-color="#7d8a5a"/></linearGradient>
        <linearGradient id="a-earth" x1="0" y1="0" x2="0" y2="1"><stop offset="0" stop-color="#8fb4dc"/><stop offset="0.45" stop-color="#5b7a45"/><stop offset="0.6" stop-color="#c47a50"/><stop offset="1" stop-color="#b35d3a"/></linearGradient>
        <linearGradient id="a-rig" x1="0" y1="0" x2="0" y2="1"><stop offset="0" stop-color="#5a87c2"/><stop offset="0.6" stop-color="#c9cdd2"/><stop offset="1" stop-color="#8a8a6a"/></linearGradient>
      </defs>
      <polygon points="0,392 170,445 0,487" fill="#1c1c1c"/>
      <polygon points="0,487 469,385 469,393 0,508" fill="#d8222a"/>
      <polygon points="0,515 230,459 230,566 0,622" fill="url(#a-plant)" role="img" aria-label="Photo: power plant with smokestacks during demolition"/>
      <polygon points="240,456 469,400 469,504 240,563" fill="url(#a-site)" role="img" aria-label="Photo: aerial view of industrial conveyor facility"/>
      <polygon points="0,628 230,572 230,691 0,740" fill="url(#a-earth)" role="img" aria-label="Photo: earthmoving equipment grading a red clay site"/>
      <polygon points="240,569 469,510 469,640 240,689" fill="url(#a-rig)" role="img" aria-label="Photo: yellow excavator beside a launch facility"/>
      <polygon points="300,687 469,646 469,740" fill="#1c1c1c"/>
      <polygon points="0,742 469,640 469,652 0,750" fill="#d8222a"/>
    </svg>
    <p class="website">WWW.RKHALDEN.COM</p>
    <span class="website__rule"></span>
  </section>

  <section class="banner banner--second">
    <div class="banner__topbar"></div>
    <div class="brand"><span class="brand__name">R.K. HALDEN</span><span class="brand__sub">Companies</span></div>
    <h2 class="headline headline--lead">Shaping America’s</h2>
    <h1 class="headline headline--main">Skyline</h1>
    <p class="headline headline--since">Since 1959</p>
    <span class="rule rule--left"></span><span class="rule rule--right"></span>
    <div class="phone">
      <svg viewBox="0 0 24 24" aria-hidden="true"><circle cx="12" cy="12" r="12" fill="#fff"/><path d="M8.2 6.5l1.9-.4 1.2 3-1.3 1c.6 1.4 1.6 2.5 3 3.2l1-1.3 3 1.2-.4 1.9c-4.4.4-8.7-3.9-8.4-8.6z" fill="#d8222a"/></svg>
      <span>888-555-0142</span>
    </div>
    <svg class="graphic graphic--mirrored" viewBox="0 0 469 783">
      <defs>
        <linearGradient id="b-wreck" x1="0" y1="0" x2="0" y2="1"><stop offset="0" stop-color="#dfe3e6"/><stop offset="0.5" stop-color="#d44b3a"/><stop offset="1" stop-color="#c9a040"/></linearGradient>
        <linearGradient id="b-dig" x1="0" y1="0" x2="0" y2="1"><stop offset="0" stop-color="#8fb0d4"/><stop offset="0.45" stop-color="#4f7a3f"/><stop offset="1" stop-color="#b8643c"/></linearGradient>
        <linearGradient id="b-grade" x1="0" y1="0" x2="0" y2="1"><stop offset="0" stop-color="#6f9bd6"/><stop offset="0.45" stop-color="#4a6b3a"/><stop offset="0.6" stop-color="#d49a78"/><stop offset="1" stop-color="#c98560"/></linearGradient>
        <linearGradient id="b-ruin" x1="0" y1="0" x2="0" y2="1"><stop offset="0" stop-color="#c8d4de"/><stop offset="0.5" stop-color="#7f8690"/><stop offset="1" stop-color="#c7c9b8"/></linearGradient>
      </defs>
      <polygon points="0,392 170,445 0,487" fill="#1c1c1c"/>
      <polygon points="0,487 469,385 469,393 0,508" fill="#d8222a"/>
      <polygon points="0,515 230,459 230,566 0,622" fill="url(#b-wreck)" role="img" aria-label="Photo: excavator dismantling a red industrial building"/>
      <polygon points="240,456 469,400 469,504 240,563" fill="url(#b-dig)" role="img" aria-label="Photo: excavators loading a truck on a dirt mound"/>
      <polygon points="0,628 230,572 230,691 0,740" fill="url(#b-grade)" role="img" aria-label="Photo: haul trucks and dozers working a cleared site"/>
      <polygon points="240,569 469,510 469,640 240,689" fill="url(#b-ruin)" role="img" aria-label="Photo: partially demolished industrial plant with debris"/>
      <polygon points="300,687 469,646 469,740" fill="#1c1c1c"/>
      <polygon points="0,742 469,640 469,652 0,750" fill="#d8222a"/>
    </svg>
    <p class="website">WWW.RKHALDEN.COM</p>
    <span class="website__rule"></span>
  </section>

</main>
</body>
</html>
```